Website for Private Psychologist

DO NOT CONTACT ME PRIVATELY

I am a Psychologist offering psychotherapy for individuals and couples, and clinical consultation and training and education for mental and medical health professionals and agencies.

I need a redesign of my website

5 Pages (content is attached for each page)
Home
Jungian Psychotherapy
Clinical Consultation & Professional Development
Curriculum Vitae & Publications
Practice Policies and Forms

Designs can be based on these style websites
https://velmorcare.info; https://brantomind.org/; https://dorelhaskettpsychotherapy.com/

Minimalist Layout: Clean and uncluttered layout with generous white space, allowing the content and visuals to stand out'

Keep a linear, uncluttered, professional design.

Please use only royalty free images and google fonts. Please provide links to any stock images used to verify license.

private individual or couples seeking psychotherapy

Psychotherapy

5+ page

• No search feature

```html
<!DOCTYPE html>
<html lang="en">
<head>
<meta charset="utf-8">
<title>Maren Holloway, PhD — Website Pages</title>
<link href="https://fonts.googleapis.com/css2?family=Jost:wght@300;400;500&display=swap" rel="stylesheet">
<style>
  :root{
    --board:#bcd2ee;
    --paper:#fbfbfb;
    --blue:#2d5d95;
    --blue-light:#4d86c6;
    --ink:#3c3f44;
    --muted:#8a8e94;
    --line:#c9cdd2;
    --photo-dark:#5d6166;
    --photo-mid:#9a9ea3;
    --photo-light:#cfd1d4;
    --white:#ffffff;
  }
  *{box-sizing:border-box;margin:0;padding:0}
  html,body{width:1200px;height:790px;overflow:hidden;background:var(--board);font-family:"Jost",sans-serif;color:var(--ink)}
  .board{position:relative;width:1200px;height:790px}
  .page{position:absolute;background:var(--paper);box-shadow:0 1px 4px rgba(30,60,100,.18);overflow:hidden}
  .abs{position:absolute}

  .site-nav{position:absolute;left:0;top:0;right:0;height:14px;display:flex;align-items:center;padding:0 7px;gap:6px;border-bottom:0.5px solid var(--line)}
  .brand{font-size:4px;font-weight:500;color:var(--blue);line-height:1;display:flex;align-items:center;gap:2px;width:46px;white-space:nowrap}
  .brand i{display:inline-block;width:3px;height:3px;background:var(--blue)}
  .nav-links{display:flex;gap:6px;font-size:2.6px;color:var(--muted);flex:1}
  .nav-btn{font-size:2.6px;border:0.4px solid var(--blue);color:var(--blue);border-radius:3px;padding:1px 4px}

  .title{font-weight:400;color:var(--blue);text-transform:uppercase;line-height:1.05;letter-spacing:.1px}
  .title .soft{color:var(--blue-light)}
  .heading{font-size:5.2px;font-weight:500;color:var(--blue);text-transform:uppercase;letter-spacing:.2px}
  .copy{font-size:2.7px;line-height:1.45;color:var(--ink)}
  .copy.muted{color:var(--muted)}
  .quote{font-size:4px;line-height:1.35;text-align:center;color:var(--ink)}
  .btn{display:inline-block;background:var(--blue);color:var(--white);font-size:2.8px;padding:2px 6px;border-radius:4px}
  .btn.ghost{background:none;border:0.4px solid var(--blue);color:var(--blue)}

  .photo{position:absolute;background:linear-gradient(135deg,var(--photo-light),var(--photo-mid))}
  .photo.dark{background:linear-gradient(135deg,var(--photo-mid),var(--photo-dark))}
  .photo.round{border-radius:50%}

  .badge{position:absolute;border-radius:50%;border:0.5px solid var(--line);display:flex;flex-direction:column;align-items:center;justify-content:center;text-align:center;padding:5px;background:var(--paper)}
  .badge b{font-size:3.4px;font-weight:500;color:var(--blue);line-height:1.2}
  .badge span{font-size:2.3px;color:var(--muted);line-height:1.35;margin-top:1px}
  .badge.filled{background:var(--blue);border-color:var(--blue)}
  .badge.filled b,.badge.filled span{color:var(--white)}

  .rows .row{display:flex;justify-content:space-between;font-size:2.6px;border-bottom:0.4px solid var(--line);padding:1.6px 0;color:var(--ink)}
  .rows .row em{font-style:normal;color:var(--blue)}

  .contact{position:absolute;left:0;right:0;bottom:0;background:var(--blue);color:var(--white);padding:10px 10px 8px;overflow:hidden}
  .contact .heading{color:var(--white)}
  .contact .ring{position:absolute;border-radius:50%;border:0.5px solid rgba(255,255,255,.35)}
  .contact-form{margin-top:5px;width:46%}
  .field{font-size:2.5px;color:rgba(255,255,255,.8);border-bottom:0.4px solid rgba(255,255,255,.55);padding:1.5px 0 1px;margin-bottom:2.5px}
  .field.tall{height:9px}
  .check{font-size:2.3px;display:flex;align-items:center;gap:2px;margin:2px 0 3px;color:rgba(255,255,255,.85)}
  .check i{width:3px;height:3px;border:0.4px solid var(--white);display:inline-block}
  .send{display:inline-block;background:var(--white);color:var(--blue);font-size:2.7px;padding:1.6px 8px;border-radius:4px}
  .contact-card{position:absolute;border-radius:50%;background:var(--white);color:var(--ink);display:flex;flex-direction:column;align-items:center;justify-content:center;text-align:center}
  .contact-card b{font-size:4px;font-weight:500;color:var(--blue)}
  .contact-card span{font-size:2.2px;line-height:1.5;color:var(--muted)}
  .foot{position:absolute;left:10px;right:10px;bottom:6px;display:flex;justify-content:space-between;align-items:flex-end;font-size:2.4px;color:rgba(255,255,255,.8)}
  .foot .cols{display:flex;gap:8px}
  .foot .cols div{line-height:1.6}
</style>
</head>
<body>
<main class="board">

  <!-- HOME -->
  <section class="page page-home" style="left:36px;top:36px;width:217px;height:736px">
    <header class="site-nav"><div class="brand"><i></i>Maren Holloway, PhD</div><nav class="nav-links"><span>Home</span><span>Jungian</span><span>Consultation</span><span>CV</span><span>Policies</span></nav><span class="nav-btn">Contact</span></header>

    <h1 class="title abs" style="left:10px;top:24px;font-size:8.6px">Jungian<br>Psychotherapy<br>&amp; Consultation</h1>
    <p class="copy abs" style="left:10px;top:56px;width:92px">Psychotherapy for individuals and couples, and clinical consultation, training and education for mental and medical health professionals and agencies.</p>
    <span class="btn abs" style="left:10px;top:84px">Book a session</span>
    <div class="photo abs" role="img" aria-label="Black and white photo of two hands reaching toward each other" style="left:112px;top:20px;width:94px;height:82px"></div>

    <div class="badge" style="left:12px;top:138px;width:40px;height:40px"><b>15+</b><span>years in practice</span></div>
    <div class="badge" style="left:63px;top:138px;width:40px;height:40px"><b>Couples</b><span>and individuals</span></div>
    <div class="badge filled" style="left:114px;top:138px;width:40px;height:40px"><b>Jungian</b><span>analytic approach</span></div>
    <div class="badge" style="left:165px;top:138px;width:40px;height:40px"><b>Training</b><span>for clinicians</span></div>

    <div class="photo dark" role="img" aria-label="Photo of a suspension bridge over the bay" style="left:10px;top:190px;width:46px;height:56px"></div>
    <div class="photo" role="img" aria-label="Portrait photo of the psychologist" style="left:59px;top:190px;width:46px;height:56px"></div>
    <h2 class="heading abs" style="left:112px;top:192px">About me</h2>
    <p class="copy abs" style="left:112px;top:202px;width:94px">I am a licensed psychologist and Jungian analyst. My work draws on depth psychology, dreams and the symbolic life to support lasting change. I also teach and consult with clinicians and agencies.</p>

    <p class="quote abs" style="left:26px;top:266px;width:165px">Learn how depth-oriented psychotherapy and clinical consultation can support your journey toward meaningful growth.</p>

    <h2 class="heading abs" style="left:10px;top:300px">Services</h2>
    <div class="photo" role="img" aria-label="Photo of a quiet therapy room" style="left:10px;top:312px;width:62px;height:24px"></div>
    <div class="photo dark" role="img" aria-label="Photo of a couple talking" style="left:77px;top:312px;width:62px;height:24px"></div>
    <div class="photo" role="img" aria-label="Photo of a seminar group" style="left:144px;top:312px;width:62px;height:24px"></div>
    <p class="copy abs" style="left:10px;top:339px;width:62px"><b>Jungian therapy</b><br>Long-term depth work.</p>
    <p class="copy abs" style="left:77px;top:339px;width:62px"><b>Couples work</b><br>Shared understanding.</p>
    <p class="copy abs" style="left:144px;top:339px;width:62px"><b>Consultation</b><br>For professionals.</p>

    <h2 class="heading abs" style="left:10px;top:376px">Formats</h2>
    <div class="photo" role="img" aria-label="Photo of a laptop for online sessions" style="left:10px;top:388px;width:72px;height:30px"></div>
    <p class="copy abs" style="left:90px;top:390px;width:112px"><b style="color:var(--blue);font-size:3.4px;font-weight:500">Online sessions</b><br>Secure video sessions for clients across the state.</p>
    <p class="copy abs" style="left:10px;top:426px;width:112px"><b style="color:var(--blue);font-size:3.4px;font-weight:500">Office sessions</b><br>In-person meetings in a calm private office.</p>
    <div class="photo dark" role="img" aria-label="Photo of an office with armchairs" style="left:134px;top:422px;width:72px;height:30px"></div>

    <h2 class="heading abs" style="left:10px;top:474px">Practice policies and forms</h2>
    <p class="copy muted abs" style="left:10px;top:484px;width:196px">Please review the policies and complete intake forms before your first appointment.</p>
    <div class="badge" style="left:12px;top:498px;width:44px;height:44px"><b>Fees</b><span>and insurance</span></div>
    <div class="badge" style="left:61px;top:498px;width:44px;height:44px"><b>Intake</b><span>forms</span></div>
    <div class="badge filled" style="left:110px;top:498px;width:44px;height:44px"><b>Privacy</b><span>practices</span></div>
    <div class="badge" style="left:159px;top:498px;width:44px;height:44px"><b>Cancel</b><span>policy</span></div>

    <footer class="contact" style="height:160px">
      <span class="ring" style="left:150px;top:-40px;width:120px;height:120px"></span>
      <h2 class="heading">Contact me</h2>
      <form class="contact-form">
        <div class="field">Name</div><div class="field">Email</div><div class="field">Phone</div><div class="field tall">Message</div>
        <div class="check"><i></i>I agree to the privacy policy</div>
        <span class="send">Send</span>
      </form>
      <div class="contact-card" style="left:122px;top:20px;width:58px;height:58px"><b>Contact</b><span>Office hours<br>Mon–Fri, 9–6<br>velmorcare.info</span></div>
      <div class="foot"><span>© Maren Holloway 2024</span><div class="cols"><div>Home<br>Jungian<br>Consulting</div><div>CV<br>Policies<br>Contact</div></div></div>
    </footer>
  </section>

  <!-- JUNGIAN PSYCHOTHERAPY -->
  <section class="page page-jungian" style="left:267px;top:36px;width:214px;height:633px">
    <header class="site-nav"><div class="brand"><i></i>Maren Holloway, PhD</div><nav class="nav-links"><span>Home</span><span>Jungian</span><span>Consultation</span><span>CV</span><span>Policies</span></nav><span class="nav-btn">Contact</span></header>
    <div class="photo dark abs" role="img" aria-label="Dark photo of hands folded in a session" style="left:0;top:14px;width:214px;height:56px"></div>
    <h1 class="title abs" style="left:10px;top:80px;font-size:7.6px">Jungian<br>Psychotherapy</h1>
    <p class="copy abs" style="left:108px;top:80px;width:96px">Jungian therapy explores the unconscious through dreams, images and the stories that shape a life.</p>
    <p class="quote abs" style="left:28px;top:108px;width:158px">Jungian therapy is a form of psychodynamic therapy which, according to a study, has been found to be as effective as cognitive behavioural therapy and medication for treating depression.</p>

    <div class="photo abs" role="img" aria-label="Photo of a person writing in a journal" style="left:10px;top:156px;width:80px;height:36px"></div>
    <h2 class="heading abs" style="left:98px;top:158px">Idea</h2>
    <p class="copy abs" style="left:98px;top:167px;width:106px">The psyche seeks wholeness. Therapy helps bring hidden parts of the self into awareness so they can be lived more fully.</p>

    <h2 class="heading abs" style="left:10px;top:204px">Help</h2>
    <p class="copy abs" style="left:10px;top:213px;width:104px">Sessions support people facing depression, anxiety, loss, relationship difficulty and questions of meaning.</p>
    <div class="photo dark abs" role="img" aria-label="Photo of clasped hands" style="left:124px;top:200px;width:80px;height:38px"></div>

    <h2 class="heading abs" style="left:10px;top:250px">Efficiency</h2>
    <p class="copy muted abs" style="left:10px;top:259px;width:194px">Research shows depth therapy brings benefits that continue to grow after treatment ends.</p>
    <div class="badge" style="left:22px;top:270px;width:44px;height:44px"><b>Lasting</b><span>results over time</span></div>
    <div class="badge filled" style="left:85px;top:270px;width:44px;height:44px"><b>Effective</b><span>as other methods</span></div>
    <div class="badge" style="left:148px;top:270px;width:44px;height:44px"><b>Growth</b><span>beyond symptoms</span></div>

    <h2 class="heading abs" style="left:10px;top:326px">Resources</h2>
    <p class="copy abs" style="left:10px;top:335px;width:140px">Learn more about analytic training and community events at brantomind.org.</p>
    <span class="btn ghost abs" style="left:10px;top:348px">Read more</span>
    <div class="photo dark round abs" role="img" aria-label="Round photo of a stack of books" style="left:168px;top:318px;width:32px;height:32px"></div>

    <footer class="contact" style="height:166px">
      <span class="ring" style="left:140px;top:-30px;width:130px;height:130px"></span>
      <h2 class="heading">Contact me</h2>
      <form class="contact-form">
        <div class="field">Name</div><div class="field">Email</div><div class="field">Phone</div><div class="field tall">Message</div>
        <div class="check"><i></i>I agree to the privacy policy</div>
        <span class="send">Send</span>
      </form>
      <div class="contact-card" style="left:120px;top:22px;width:58px;height:58px"><b>Contact</b><span>Office hours<br>Mon–Fri, 9–6<br>velmorcare.info</span></div>
      <div class="foot"><span>© Maren Holloway 2024</span><div class="cols"><div>Home<br>Jungian<br>Consulting</div><div>CV<br>Policies<br>Contact</div></div></div>
    </footer>
  </section>

  <!-- CONSULTATION -->
  <section class="page page-consult" style="left:499px;top:36px;width:209px;height:330px">
    <header class="site-nav"><div class="brand"><i></i>Maren Holloway, PhD</div><nav class="nav-links"><span>Home</span><span>Jungian</span><span>Consultation</span><span>CV</span><span>Policies</span></nav><span class="nav-btn">Contact</span></header>
    <div class="photo abs" role="img" aria-label="Photo of colleagues in a meeting" style="left:8px;top:20px;width:42px;height:18px"></div>
    <div class="photo dark abs" role="img" aria-label="Photo of a lecture hall" style="left:8px;top:41px;width:42px;height:18px"></div>
    <h1 class="title abs" style="left:56px;top:20px;font-size:7.6px"><span class="soft">Clinical</span> Consultation<br>&amp; Professional<br>Development</h1>
    <p class="copy abs" style="left:56px;top:49px;width:142px">Case consultation, supervision and training for clinicians, medical teams and agencies.</p>

    <h2 class="heading abs" style="left:8px;top:74px">Questions &amp; answers</h2>
    <div class="rows abs" style="left:8px;top:83px;width:92px">
      <div class="row">Who is it for?<em>+</em></div><div class="row">Individual sessions<em>+</em></div><div class="row">Group consultation<em>+</em></div><div class="row">Agency training<em>+</em></div><div class="row">Fees<em>+</em></div>
    </div>
    <div class="rows abs" style="left:108px;top:83px;width:92px">
      <div class="row">Online or in person<em>+</em></div><div class="row">Continuing education<em>+</em></div><div class="row">Topics offered<em>+</em></div><div class="row">Scheduling<em>+</em></div><div class="row">Contact<em>+</em></div>
    </div>
    <span class="btn ghost abs" style="left:8px;top:126px">Request consultation</span>

    <footer class="contact" style="height:180px">
      <span class="ring" style="left:140px;top:-30px;width:110px;height:110px"></span>
      <h2 class="heading">Contact me</h2>
      <form class="contact-form">
        <div class="field">Name</div><div class="field">Email</div><div class="field">Phone</div><div class="field tall">Message</div>
        <span class="send">Send</span>
      </form>
      <div class="contact-card" style="left:112px;top:20px;width:56px;height:56px"><b>Contact</b><span>Office hours<br>Mon–Fri, 9–6</span></div>
      <div class="foot"><span>© Maren Holloway 2024</span></div>
    </footer>
  </section>

  <!-- CV -->
  <section class="page page-cv" style="left:727px;top:53px;width:209px;height:500px">
    <header class="site-nav"><div class="brand"><i></i>Maren Holloway, PhD</div><nav class="nav-links"><span>Home</span><span>Jungian</span><span>Consultation</span><span>CV</span><span>Policies</span></nav><span class="nav-btn">Contact</span></header>
    <div class="photo dark abs" role="img" aria-label="Photo of a suspension bridge in fog" style="left:0;top:14px;width:209px;height:66px"></div>
    <div class="photo round abs" role="img" aria-label="Round portrait photo of the psychologist" style="left:148px;top:48px;width:46px;height:46px;border:2px solid var(--paper)"></div>
    <h1 class="title abs" style="left:10px;top:88px;font-size:7.6px">Curriculum Vitae<br>&amp; Publications</h1>
    <p class="copy abs" style="left:10px;top:108px;width:124px">Licensed psychologist and Jungian analyst with over fifteen years of clinical, teaching and consulting experience.</p>
    <span class="btn abs" style="left:148px;top:104px">Download CV</span>
    <span class="btn ghost abs" style="left:148px;top:114px">Contact</span>

    <h2 class="heading abs" style="left:10px;top:142px">Prior professional experience</h2>
    <p class="copy abs" style="left:10px;top:152px;width:190px">Senior faculty member and training analyst, teaching seminars on dreams, complexes and clinical practice. Staff psychologist in a community clinic serving adults and couples. Consultant to hospital teams on trauma informed care and staff wellbeing. Supervisor for doctoral trainees and fellows.</p>

    <h2 class="heading abs" style="left:10px;top:212px">Publications</h2>
    <span class="abs" style="left:184px;top:212px;font-size:3.4px;color:var(--blue)">‹ ›</span>
    <div class="photo abs" role="img" aria-label="Book cover photo" style="left:10px;top:222px;width:28px;height:22px"></div>
    <div class="photo dark abs" role="img" aria-label="Book cover photo" style="left:42px;top:222px;width:28px;height:22px"></div>
    <div class="photo abs" role="img" aria-label="Book cover photo" style="left:74px;top:222px;width:28px;height:22px"></div>
    <div class="photo dark abs" role="img" aria-label="Book cover photo" style="left:106px;top:222px;width:28px;height:22px"></div>
    <div class="photo abs" role="img" aria-label="Book cover photo" style="left:138px;top:222px;width:28px;height:22px"></div>
    <div class="photo dark abs" role="img" aria-label="Book cover photo" style="left:170px;top:222px;width:29px;height:22px"></div>
    <p class="copy muted abs" style="left:10px;top:247px;width:190px">Selected articles and chapters, 2008–2024</p>

    <footer class="contact" style="height:228px">
      <span class="ring" style="left:130px;top:-30px;width:120px;height:120px"></span>
      <h2 class="heading">Contact me</h2>
      <form class="contact-form">
        <div class="field">Name</div><div class="field">Email</div><div class="field">Phone</div><div class="field tall">Message</div>
        <div class="check"><i></i>I agree to the privacy policy</div>
        <span class="send">Send</span>
      </form>
      <div class="contact-card" style="left:112px;top:24px;width:58px;height:58px"><b>Contact</b><span>Office hours<br>Mon–Fri, 9–6<br>velmorcare.info</span></div>
      <div class="foot"><span>© Maren Holloway 2024</span><div class="cols"><div>Home<br>Jungian<br>Consulting</div><div>CV<br>Policies<br>Contact</div></div></div>
    </footer>
  </section>

  <!-- POLICIES -->
  <section class="page page-policies" style="left:957px;top:36px;width:210px;height:392px">
    <header class="site-nav"><div class="brand"><i></i>Maren Holloway, PhD</div><nav class="nav-links"><span>Home</span><span>Jungian</span><span>Consultation</span><span>CV</span><span>Policies</span></nav><span class="nav-btn">Contact</span></header>
    <h1 class="title abs" style="left:10px;top:24px;font-size:7.6px">Practice policies and<br>forms</h1>
    <div class="badge" style="left:16px;top:58px;width:70px;height:70px"><b>Fee Policy and<br>Cancellation Policies</b><span>Session fees, billing and notice required for changes.</span></div>
    <div class="badge filled" style="left:112px;top:44px;width:76px;height:76px"><b>The Informed Consent</b><span>Please read and sign before your first session.</span></div>
    <div class="badge" style="left:16px;top:136px;width:70px;height:70px"><b>Our Good Faith<br>Estimate Notice</b><span>Your right to a cost estimate.</span></div>
    <div class="badge" style="left:112px;top:130px;width:76px;height:76px"><b>California Notice of<br>Psychology Complaint<br>Policy</b><span>How to raise a concern.</span></div>

    <footer class="contact" style="height:160px">
      <span class="ring" style="left:130px;top:-30px;width:110px;height:110px"></span>
      <h2 class="heading">Contact me</h2>
      <form class="contact-form">
        <div class="field">Name</div><div class="field">Email</div><div class="field">Phone</div><div class="field tall">Message</div>
        <span class="send">Send</span>
      </form>
      <div class="contact-card" style="left:114px;top:20px;width:56px;height:56px"><b>Contact</b><span>Office hours<br>Mon–Fri, 9–6</span></div>
      <div class="foot"><span>© Maren Holloway 2024</span></div>
    </footer>
  </section>

</main>
</body>
</html>
```